Summer Fun

I need a Poster for Front of hotel advertising discounted drinks on Thursday & Fridays
$3.50.
Schooners of Local Beer, Glass of House Wine & Bubbly.
From 3.30pm to 6.30 pm
Nibblies Provided

Target Market(s)

25 + Market

Industry/Entity Type

Hotel

Requirements
Should not have
• Do not want to be known as Happy Hour.

```html
<!DOCTYPE html>
<html lang="en">
<head>
<meta charset="utf-8">
<title>Discount Drinks Poster</title>
<link rel="stylesheet" href="https://fonts.googleapis.com/css2?family=Archivo+Black&family=Oswald:wght@700&family=Arimo:wght@700&family=Orbitron:wght@500&display=swap">
<style>
  :root {
    --cork: #9c7650;
    --cork-light: #b48d63;
    --cork-dark: #7e5c3c;
    --ink: #121212;
    --note: #f6ef8a;
    --note-shade: #e9df6c;
    --bottle-green: #3f9a2a;
    --bottle-light: #8fd04a;
    --bottle-dark: #1d4a12;
    --amber: #b98a1f;
    --sign-red: #7a0f12;
    --sign-deep: #3e0507;
    --sign-glow: #ff6a6a;
    --ring: #e8e2dc;
    --pin: #3fae3a;
  }
  html, body { margin: 0; padding: 0; overflow: hidden; }
  body { width: 849px; height: 1200px; }
  .poster {
    position: relative;
    width: 849px;
    height: 1200px;
    overflow: hidden;
    background: radial-gradient(ellipse at 40% 45%, var(--cork-light), var(--cork) 55%, var(--cork-dark));
  }
  .bottle-row {
    position: absolute;
    left: 0; top: 0;
    width: 849px; height: 170px;
    background: linear-gradient(180deg, var(--bottle-dark) 0%, var(--bottle-green) 45%, var(--bottle-light) 80%, rgba(143,208,74,0) 100%);
  }
  .headline {
    position: absolute;
    left: 26px; top: 150px;
    margin: 0;
    font-family: "Archivo Black", sans-serif;
    font-weight: 400;
    color: var(--ink);
    font-size: 140px;
    line-height: 0.88;
    letter-spacing: -6px;
    text-transform: uppercase;
    white-space: nowrap;
  }
  .bottles-left {
    position: absolute;
    left: 0; top: 880px;
    width: 470px; height: 320px;
    background: linear-gradient(90deg, var(--bottle-light) 0%, var(--bottle-dark) 25%, var(--amber) 55%, var(--bottle-green) 80%, var(--amber) 100%);
    clip-path: polygon(0 30%, 20% 0, 32% 20%, 45% 5%, 60% 30%, 72% 22%, 88% 18%, 100% 35%, 100% 100%, 0 100%);
  }
  .bottles-right {
    position: absolute;
    left: 470px; top: 690px;
    width: 379px; height: 510px;
    background: linear-gradient(120deg, var(--bottle-light) 0%, var(--bottle-green) 40%, var(--bottle-dark) 100%);
    clip-path: polygon(0 6%, 18% 0, 34% 28%, 58% 8%, 74% 0, 100% 24%, 100% 100%, 8% 100%, 2% 50%);
  }
  .note {
    position: absolute;
    z-index: 2;
    left: 26px; top: 492px;
    width: 440px; height: 370px;
    background: linear-gradient(160deg, var(--note) 70%, var(--note-shade));
    transform: rotate(-0.6deg);
    box-shadow: 3px 5px 10px rgba(0,0,0,0.35);
    box-sizing: border-box;
    padding: 24px 22px 0 22px;
  }
  .note-days {
    margin: 0;
    font-family: "Oswald", sans-serif;
    font-weight: 700;
    font-size: 56px;
    line-height: 0.98;
    color: var(--ink);
    text-transform: uppercase;
    white-space: nowrap;
  }
  .note-list {
    list-style: none;
    margin: 16px 0 0;
    padding: 0;
    font-family: "Arimo", sans-serif;
    font-weight: 700;
    font-size: 30px;
    line-height: 1.55;
    color: var(--ink);
    letter-spacing: -0.5px;
    white-space: nowrap;
  }
  .note-price {
    position: absolute;
    right: 60px; bottom: 26px;
    font-family: "Arimo", sans-serif;
    font-weight: 700;
    font-size: 46px;
    color: var(--ink);
  }
  .pin {
    position: absolute;
    z-index: 3;
    left: 236px; top: 470px;
    width: 36px; height: 36px;
  }
  .time-sign {
    position: absolute;
    left: 530px; top: 345px;
    width: 300px; height: 300px;
    border-radius: 50%;
    background: var(--ring);
    box-shadow: 3px 6px 14px rgba(0,0,0,0.45);
  }
  .time-face {
    position: absolute;
    inset: 10px;
    border-radius: 50%;
    background: radial-gradient(circle at 45% 40%, var(--sign-red), var(--sign-deep));
    display: flex;
    flex-direction: column;
    align-items: center;
    justify-content: center;
    font-family: "Orbitron", sans-serif;
    color: var(--sign-glow);
    text-shadow: 0 0 6px rgba(255,80,80,0.7);
  }
  .time-big { font-size: 52px; line-height: 1.05; font-weight: 500; }
  .time-small { font-size: 24px; line-height: 1.1; }
</style>
</head>
<body>
<main class="poster">
  <div class="bottle-row" role="img" aria-label="Row of green beer bottle necks along the top edge"></div>

  <h1 class="headline">Discount<br>Drinks*</h1>

  <div class="bottles-left" role="img" aria-label="Wine and beer bottles in green and amber glass"></div>
  <div class="bottles-right" role="img" aria-label="Two green beer bottles angled up from the bottom right"></div>

  <section class="note">
    <h2 class="note-days">Thursdays<br>and Fridays</h2>
    <ul class="note-list">
      <li>Schooners of local beer</li>
      <li>Glass of house wine</li>
      <li>Bubbly</li>
    </ul>
    <div class="note-price">$3.50</div>
  </section>

  <svg class="pin" viewBox="0 0 34 34" aria-hidden="true">
    <circle cx="17" cy="17" r="15" fill="var(--pin)"/>
    <circle cx="13" cy="12" r="5" fill="#9be38f"/>
  </svg>

  <div class="time-sign">
    <div class="time-face">
      <span class="time-big">3:30pm</span>
      <span class="time-small">untill</span>
      <span class="time-big">6:30pm</span>
    </div>
  </div>
</main>
</body>
</html>
```